Business Card Design Project

Hello Designers, hope you are all aiming enjoy the weekend
I have the Business Logo (uploaded), you can alter the color which ever way you think would work,
Im looking for a simple yet striking feel, something which will stay memorable (I have uploaded 3 examples for you to flick through)
Information on the card, will just be the bare minimum,
Double Sided
Info being
i.e.
Name
Number
Website
ABN
Tobin Wexmoor
+468213579 (singapore)
+315792846 (Australia)
+729384615 (America)
www.lomevu-linkup.example
ABN 86420913
Enjoy,
Tobin
Industry/Entity Type
Business
Look and feel
Each slider illustrates characteristics of the customer's brand and the style your logo design should communicate.

```html
<!DOCTYPE html>
<html lang="en">
<head>
<meta charset="utf-8">
<title>Tobin Wexmoor – Business Card</title>
<link rel="stylesheet" href="https://fonts.googleapis.com/css2?family=Inter:wght@400;800&display=swap">
<style>
  :root {
    --card-red: #a51c33;
    --card-ink: #ffffff;
    --mark-red: #c22a44;
    --page-bg: #ecebe8;
    --card-shadow: rgba(0, 0, 0, 0.18);
  }
  * { box-sizing: border-box; margin: 0; padding: 0; }
  html, body {
    width: 1200px;
    height: 900px;
    overflow: hidden;
  }
  body {
    background: var(--page-bg);
    font-family: "Inter", "Helvetica Neue", Arial, sans-serif;
    display: flex;
    flex-direction: column;
    align-items: center;
    justify-content: center;
    gap: 40px;
  }
  .card {
    position: relative;
    width: 720px;
    height: 411px;
    background: var(--card-red);
    color: var(--card-ink);
    box-shadow: 0 6px 18px var(--card-shadow);
  }
  .card-front__details {
    position: absolute;
    top: 34px;
    left: 32px;
    font-weight: 800;
    font-size: 37px;
    line-height: 1.02;
    letter-spacing: -0.01em;
    text-transform: uppercase;
    list-style: none;
  }
  .card-front__mark {
    position: absolute;
    right: 30px;
    bottom: 120px;
    width: 58px;
    height: 58px;
    background: var(--mark-red);
  }
  .card-back {
    display: flex;
    align-items: center;
    justify-content: center;
  }
  .brand {
    display: flex;
    align-items: center;
    gap: 12px;
  }
  .brand__square {
    width: 22px;
    height: 22px;
    background: var(--mark-red);
  }
  .brand__name {
    font-weight: 400;
    font-size: 27px;
    letter-spacing: 0.02em;
    color: var(--card-ink);
  }
</style>
</head>
<body>
  <section class="card card-front" aria-label="Card front">
    <ul class="card-front__details">
      <li class="card-front__name">Tobin Wexmoor</li>
      <li class="card-front__phone">+468213579 (Singapore)</li>
      <li class="card-front__phone">+315792846 (Australia)</li>
      <li class="card-front__phone">+729384615 (America)</li>
      <li class="card-front__web">www.lomevu-linkup.example</li>
      <li class="card-front__abn">ABN 86420913</li>
    </ul>
    <div class="card-front__mark"></div>
  </section>

  <section class="card card-back" aria-label="Card back">
    <div class="brand">
      <span class="brand__square"></span>
      <span class="brand__name">Lomevu Linkup</span>
    </div>
  </section>
</body>
</html>
```